Luxury packaging graphic design for a new Hair care elixir

We need a packaging design for a new product for our line extension of hair colouring. We have already a packaging that is very well received (all in pink) including all accesories and transport box (attached files).
For a new product - protein for the hair - we need a different design tapping into luxury segment.

Target Market(s)

This product is mainly for women between 25-65 that are looking forward to improve hair strukture and make hair looks better, nicer, softer, healthier. The product in the packaging could be used up to 2x times.

Industry/Entity Type

Hair And Beauty

Font styles to use
Serif
Sans Serif

Colors

Designer to choose colors to be used in the design.

Requirements
Must have
• The material of the packaging are carton/styropor/and glass (attached a picture of packaging design to be adapted). The components are quite small so the packaging plays a big role to increase the value of what it is inside. The packaging needs to be inline with our actual packaging designs and corporate identity as they may be delivered together so as an assamble it should look nice, beautiful and of high quality.
• The graphic design for the different components to be adapted are:
• - grapich design for outside box
• - graphic design for the inside bottles
• - graphic design for the flyer/instructions inside the box
Nice to have
• It needs to feel that the packaging is Wow! It is going to be delivered per post so there have to be a beautiful opening effect. Eventually to work with colours like black, white and gold would give a nice luxury feeling.
• The actual product inside is a concentrated protein component so it is very small, therefore the packaging should show that even if small it is an elixir for the hair.
Should not have
• a totally diffenet look as our actual designs.

```html
<!DOCTYPE html>
<html lang="en">
<head>
<meta charset="utf-8">
<title>Vela Noor – Protein Elixir Packaging</title>
<link rel="stylesheet" href="https://fonts.googleapis.com/css2?family=Arimo:wght@700&family=Montserrat:wght@400;500&display=swap">
<style>
  :root {
    --paper: #ffffff;
    --ink: #111111;
    --black: #0b0a08;
    --deep: #1c1a12;
    --olive: #3a3315;
    --gold: #c9a84a;
    --gold-light: #e6cf7e;
    --fold: rgba(179,38,30,.6);
    --pattern-base: #f3f3f3;
    --pattern-tone: #dedede;
  }
  * { margin: 0; padding: 0; box-sizing: border-box; }
  html, body { width: 1200px; height: 798px; overflow: hidden; background: var(--paper); }
  .sheet { position: relative; width: 1200px; height: 798px; }

  .spec {
    position: absolute; left: 18px; top: 26px;
    font: 700 19px "Arimo", sans-serif; color: var(--ink);
  }

  .dieline { position: absolute; left: 0; top: 0; width: 1200px; height: 798px; }

  .lid-title {
    position: absolute; left: 164px; top: 448px; width: 210px; height: 100px;
    background: radial-gradient(ellipse at 50% 50%, rgba(11,10,8,.9) 0%, rgba(11,10,8,.6) 45%, rgba(11,10,8,0) 72%);
    display: flex; flex-direction: column; align-items: center; justify-content: center;
  }
  .brand-name {
    font: 500 26px/1 "Montserrat", sans-serif; color: var(--gold);
    letter-spacing: 1px;
  }
  .brand-line {
    margin-top: 8px; font: 500 8px "Montserrat", sans-serif;
    color: var(--gold); letter-spacing: 1px;
  }

  .flyer {
    position: absolute; left: 516px; top: 128px; width: 250px; height: 592px;
    background: var(--black);
  }
  .flyer-wave {
    position: absolute; left: 4px; top: 4px; right: 4px; bottom: 4px;
    background: linear-gradient(160deg, var(--deep) 0%, var(--olive) 30%, #1a170c 55%, var(--olive) 80%, var(--deep) 100%);
  }
  .flyer-fold {
    position: absolute; left: 12px; right: 12px; border-top: 1px solid var(--fold);
  }
  .flyer-copy {
    position: absolute; left: 16px; top: 332px; width: 218px; height: 160px;
    background: rgba(8,8,6,.92);
    padding: 8px 9px;
    transform: rotate(180deg);
    color: var(--gold-light);
    font: 400 4.6px/1.45 "Montserrat", sans-serif;
    display: flex; flex-direction: column;
  }
  .flyer-copy p { margin-bottom: 5px; }
  .flyer-copy .copy-title {
    margin-top: auto; text-align: center;
    font: 500 12px/1 "Montserrat", sans-serif; color: var(--gold); letter-spacing: .8px;
  }

  .tissue {
    position: absolute; left: 798px; top: 122px; width: 355px; height: 354px;
    background:
      repeating-linear-gradient(90deg, var(--pattern-base) 0 30px, var(--pattern-tone) 30px 34px, var(--pattern-base) 34px 88px),
      var(--pattern-base);
    opacity: .85;
  }

  .bottle-label {
    position: absolute; left: 894px; top: 544px; width: 164px; height: 122px;
    border: 2px solid var(--gold);
    background: radial-gradient(ellipse at 50% 50%, #3a3834 0%, var(--black) 75%);
    display: flex; flex-direction: column; align-items: center; justify-content: center;
  }
  .bottle-label .brand-name { font-size: 22px; }
  .bottle-label .brand-line { font-size: 7.5px; margin-top: 7px; }
</style>
</head>
<body>
<main class="sheet">
  <h1 class="spec">L 170 x P 170 x A 40 mm.</h1>

  <svg class="dieline" viewBox="0 0 1500 997.5">
    <defs>
      <linearGradient id="waveGold" x1="0" y1="0" x2="1" y2="1">
        <stop offset="0" stop-color="#1c1a12"/>
        <stop offset=".3" stop-color="#3d3516"/>
        <stop offset=".5" stop-color="#17150c"/>
        <stop offset=".75" stop-color="#3d3516"/>
        <stop offset="1" stop-color="#1c1a12"/>
      </linearGradient>
    </defs>
    <g role="img" aria-label="Box dieline printed with flowing gold line waves on black">
      <polygon fill="url(#waveGold)" points="
        205,343 465,343 465,378 485,378 485,420 525,440 545,448 545,465
        560,450 600,450 600,465 645,465 645,790 600,790 600,775 560,775 545,790
        545,830 520,840 490,870 465,870 465,898 205,898 205,870 185,870 185,830
        135,790 85,790 85,775 22,775 22,465 40,465 40,448 85,448 135,460
        135,440 185,420 185,378 205,378"/>
    </g>
    <g fill="none" stroke="rgba(179,38,30,.55)" stroke-width="1">
      <rect x="135" y="485" width="410" height="275"/>
      <rect x="200" y="420" width="285" height="410"/>
    </g>
  </svg>

  <div class="lid-title">
    <span class="brand-name">vela noor</span>
    <span class="brand-line">STRENGTH IN EVERY STRAND</span>
  </div>

  <section class="flyer">
    <div class="flyer-wave" role="img" aria-label="Flowing gold line waves on black"></div>
    <div class="flyer-fold" style="top:304px"></div>
    <div class="flyer-fold" style="top:524px"></div>
    <div class="flyer-copy">
      <p>Protein elixir for hair that feels renewed. A few drops restore strength, softness and shine from root to tip. Apply to clean, damp hair, leave on for ten minutes and rinse well. Use up to twice for lasting care.</p>
      <p>How to use: shake the vial gently, mix with your conditioner or apply directly, work through lengths and ends, then comb evenly. Avoid contact with eyes. Keep in a cool, dry place away from light.</p>
      <p>Ingredients: hydrolysed keratin, wheat protein, argan oil, panthenol, water, glycerin. For external use only. Made with care for every shade of you.</p>
      <span class="copy-title">vela noor</span>
    </div>
  </section>

  <div class="tissue" role="img" aria-label="Tissue paper with a light grey ornamental pattern on white"></div>

  <div class="bottle-label">
    <span class="brand-name">vela noor</span>
    <span class="brand-line">STRENGTH IN EVERY STRAND</span>
  </div>
</main>
</body>
</html>
```